Drifting Ages Chronicle - Book Cover Design

I need a cover (front, spine, back) designed for the second edition of the historical book - Drifting Ages Chronicle. This book was created to be a more engaging supplementary resource to the dry texts of most middle and high school social studies classrooms. Although comprehensive and exhaustively researched, the book at times uses humor and irony to engage the reader. The cover should reflect this tone.

Book Title: Drifting Ages Chronicle
Subtitle: The Tales, Traditions and Turning Points of World History and the Regional Challenges of Today
Author: Noel Wickstrom
Updates

Project Deadline Extended
Reason: As multiple designers are working on adjustments and I am looking for new, creative ideas, I am extending the deadline five days. Thank you.

Project Deadline Extended
Reason: Artists are still making alterations to suggestions made and I also want to give designers a chance to submit new ideas.

Target Market(s)

Middle School and High School Teachers

Font styles to use
Serif

Colors
ec1f27
ffffff
000000

Requirements
Must have
• 1) See attachment for text for front cover, spine, back cover
• 2) Central, engaging image
Nice to have
• A subtle hint of humor, light tone
• Potentially upside down globe spinning
• Prefer black, red, white color scheme
Should not have
• Cartoonish text, images

```html
<!DOCTYPE html>
<html lang="en">
<head>
<meta charset="utf-8">
<title>Drifting Ages Chronicle – Cover</title>
<link rel="stylesheet" href="https://fonts.googleapis.com/css2?family=EB+Garamond:wght@400;500;600&family=Arimo:wght@400&family=Roboto+Condensed:wght@400;700&display=swap">
<style>
  :root {
    --red: #ec1f27;
    --maroon: #7d1416;
    --title-dark: #8a1719;
    --black: #000000;
    --white: #ffffff;
    --space-deep: #050a14;
    --space-glow: #12304a;
  }
  * { margin: 0; padding: 0; box-sizing: border-box; }
  html, body { width: 1200px; height: 864px; overflow: hidden; background: var(--black); }
  .cover { position: relative; width: 1200px; height: 864px; background: var(--black); }

  .panel { position: absolute; top: 0; height: 864px; }
  .back { left: 0; width: 568px; }
  .front { left: 622px; width: 578px; }
  .spine { left: 568px; width: 54px; background: var(--maroon); }

  .title-band { position: absolute; top: 0; left: 0; right: 0; height: 236px; background: var(--red); text-align: center; }
  .kicker { font-family: "EB Garamond", serif; font-weight: 600; font-size: 32px; letter-spacing: 26px; padding-left: 26px; line-height: 1; position: absolute; top: 38px; left: 0; right: 0; white-space: nowrap; }
  .main-title { font-family: "EB Garamond", serif; font-weight: 600; font-size: 54px; line-height: 1; position: absolute; top: 78px; left: 0; right: 0; white-space: nowrap; }
  .subtitle { font-family: "EB Garamond", serif; font-weight: 600; font-size: 15.5px; line-height: 21px; position: absolute; top: 140px; left: 0; right: 0; text-transform: uppercase; white-space: nowrap; }
  .back .title-band { color: var(--title-dark); }
  .front .title-band { color: var(--white); }

  .edition-tab { position: absolute; left: 170px; top: 205px; width: 258px; height: 31px; background: var(--maroon); border-radius: 14px 14px 0 0; color: var(--white); font-family: Arimo, sans-serif; font-size: 21px; line-height: 31px; text-align: center; }

  .blurb { position: absolute; top: 248px; left: 38px; width: 502px; color: var(--white); }
  .blurb h2 { font-family: "EB Garamond", serif; font-weight: 400; font-size: 31px; line-height: 1; margin-bottom: 10px; }
  .blurb p { font-family: Arimo, sans-serif; font-size: 14.6px; line-height: 19.5px; margin-bottom: 19px; }

  .artwork { position: absolute; top: 236px; left: 0; right: 0; bottom: 0;
    background:
      radial-gradient(circle at 235px 520px, #4fb7d8 0%, #2a7fa8 22%, #1d4f6a 30%, transparent 34%),
      radial-gradient(ellipse at 80% 25%, var(--space-glow) 0%, transparent 55%),
      radial-gradient(ellipse at 20% 40%, #0c2236 0%, transparent 50%),
      var(--space-deep); }
  .author { position: absolute; top: 268px; left: 0; right: 0; text-align: center; font-family: "EB Garamond", serif; font-weight: 400; font-size: 50px; line-height: 1.1; color: var(--white); white-space: nowrap; }

  .spine-text { position: absolute; left: 0; width: 54px; writing-mode: vertical-rl; color: var(--white); font-family: "Roboto Condensed", sans-serif; display: flex; align-items: center; white-space: nowrap; }
  .spine-title { top: 38px; font-weight: 700; font-size: 29px; letter-spacing: 0.5px; }
  .spine-edition { top: 440px; font-size: 17px; font-weight: 400; }
  .spine-author { top: 590px; font-weight: 700; font-size: 29px; letter-spacing: 1.5px; }
</style>
</head>
<body>
<div class="cover">
  <section class="panel back">
    <header class="title-band">
      <div class="kicker">DRIFTING</div>
      <div class="main-title">AGES CHRONICLE</div>
      <div class="subtitle">The tales, traditions and turning points of<br>world history and the regional challenges of today</div>
    </header>
    <div class="blurb">
      <h2>Do you know how we got to here?</h2>
      <p>Well, if you’re like 97.4% of the people walking the planet, you haven’t got a clue. Sure, you might know a bit about a couple rivers in Mesopotamia, how Theodoros wandered around Athens asking questions or how Anselm Voss got ticked off one day and nailed a really long essay to the door of a church. But to be honest (and don’t be embarrassed), you’ve got some gaps.</p>
      <p>Be dense no more. In Drifting Ages Chronicle, Noel Wickstrom once again takes you through all the major tales, traditions and turning points of world history - not just European history, but WORLD history. You’ll figure out real quick that the West might have had some crowning moments, but for the whole of human history, it’s been the Persians, the Indians, the Chinese, the Muslims or some horse peoples from the steppe that have truly turned us into the clever little creatures we are today.</p>
      <p>And while most world history books fade off once the Cold War comes to a close, this sometimes sardonic tome just gets going. Updated to include contemporary debates over topics such as Brexit, the rise of ISIS, claims to the South China Sea, the mounting refugee crisis and the controversial presidency of Carter Hollings, this second edition finishes with a distinctively comprehensive look at the 21st century challenges facing nine major regions of today’s world - Africa, Latin America, Japan, China, the Middle East, India, Russia, Europe and the United States.</p>
    </div>
  </section>

  <section class="panel spine">
    <div class="spine-text spine-title">DRIFTING AGES CHRONICLE</div>
    <div class="spine-text spine-edition">Second Edition</div>
    <div class="spine-text spine-author">NOEL WICKSTROM</div>
  </section>

  <section class="panel front">
    <div class="artwork" role="img" aria-label="Photograph of a glowing desk globe on a stand against a starry blue night-sky nebula"></div>
    <header class="title-band">
      <div class="kicker">DRIFTING</div>
      <div class="main-title">AGES CHRONICLE</div>
      <div class="subtitle">The tales, traditions and turning points of<br>world history and the regional challenges of today</div>
      <div class="edition-tab">Second Edition</div>
    </header>
    <div class="author">NOEL WICKSTROM</div>
  </section>
</div>
</body>
</html>
```